Sports nutritional supplement brand*

We need to design an integrated packaging for a sports nutritional supplement brand containing more than 30 products The design of the packaging consists of two parts, half in black color, fixed in all types, and the other half is variable. I sent you pictures containing some beautiful ideas that suit what I think of. The design must contain a place for the taste image, such as chocolate, strawberry, banana, orange, grape, watermelon The company name must be clearly visible in the middle and the location of the code and barcode

Target Market(s)

the whole world

Industry/Entity Type

Entrepreneur

Font styles to use
Decorative

Colors

Designer to choose colors to be used in the design.

Requirements
Must have
• The project consists of several types of supplements. I need each type to be different from the other in terms of a color that is constant, such as the black color and the half of the box is color changing, for example the box is made of black and red and the second box is black and yellow and the colors must be bright and 3D
Nice to have
• The outer box will be white and the box will be completely wrapped from the head neck down, not around the box There should be a small box design, a large protein box, and a protein pouch bag
Should not have

```html
<!DOCTYPE html>
<html lang="en">
<head>
<meta charset="utf-8">
<title>PULSEFORM Supplement Packaging – Banana &amp; Grape</title>
<link rel="stylesheet" href="https://fonts.googleapis.com/css2?family=Montserrat:wght@900&family=Space+Mono:wght@700&family=Bungee&display=swap">
<style>
  :root {
    --page: #ffffff;
    --black: #141414;
    --white: #ffffff;
    --banana: #f3e53c;
    --banana-deep: #d9c21f;
    --grape: #3f9b5e;
    --grape-deep: #2c7a45;
    --grape-photo: #cfe3a0;
    --banana-photo: #f1d24a;
  }

  * { margin: 0; padding: 0; box-sizing: border-box; }

  html, body {
    width: 1200px;
    height: 486px;
    overflow: hidden;
    background: var(--page);
  }

  .range {
    position: relative;
    width: 1200px;
    height: 486px;
  }

  .flavour-set {
    position: absolute;
    top: 0;
    width: 600px;
    height: 486px;
  }
  .flavour-set--banana { left: 0;   --accent: var(--banana); --accent-deep: var(--banana-deep); --photo: var(--banana-photo); }
  .flavour-set--grape  { left: 600px; --accent: var(--grape); --accent-deep: var(--grape-deep); --photo: var(--grape-photo); }

  /* ---------- pack label ---------- */
  .pack {
    position: absolute;
    overflow: hidden;
    background: var(--black);
    color: var(--white);
  }
  .pack--tub    { --s: 1;    left: 30px;  top: 150px; width: 230px; height: 250px; }
  .pack--jar    { --s: 0.58; left: 275px; top: 230px; width: 130px; height: 170px; }
  .pack--pouch  { --s: 0.9;  left: 420px; top: 50px;  width: 170px; height: 350px; }

  .pack-bg {
    position: absolute;
    inset: 0;
    width: 100%;
    height: 100%;
  }
  .pack-bg .band-black { fill: var(--black); }
  .pack-bg .band-accent { fill: var(--accent); }
  .pack-bg .band-white { fill: var(--white); }

  .brand {
    position: absolute;
    left: 0; right: 0;
    top: 20%;
    text-align: center;
    font-family: "Montserrat", sans-serif;
    font-weight: 900;
    font-size: calc(26px * var(--s));
    letter-spacing: 0.02em;
    color: var(--white);
  }
  .pack--pouch .brand { top: 16%; }

  .desc {
    position: absolute;
    left: 0; right: 0;
    top: 33%;
    text-align: center;
    font-family: "Space Mono", monospace;
    font-weight: 700;
    font-size: calc(9px * var(--s));
    letter-spacing: 0.04em;
    color: var(--accent);
  }
  .pack--pouch .desc { top: 25%; }

  .flavour-photo {
    position: absolute;
    left: 7%;
    top: 47%;
    width: calc(96px * var(--s));
    height: calc(84px * var(--s));
    background: var(--white);
    clip-path: polygon(25% 0, 75% 0, 100% 50%, 75% 100%, 25% 100%, 0 50%);
  }
  .flavour-photo::after {
    content: "";
    position: absolute;
    inset: 10%;
    background: radial-gradient(circle at 45% 45%, var(--photo), var(--accent-deep) 90%);
    clip-path: polygon(25% 0, 75% 0, 100% 50%, 75% 100%, 25% 100%, 0 50%);
  }
  .pack--pouch .flavour-photo { top: 40%; left: 8%; }

  .facts {
    position: absolute;
    right: 6%;
    top: 55%;
    list-style: none;
    display: flex;
    flex-direction: column;
    align-items: center;
    gap: calc(4px * var(--s));
  }
  .pack--pouch .facts { top: 55%; right: 8%; gap: calc(8px * var(--s)); }

  .fact {
    display: flex;
    flex-direction: column;
    align-items: center;
    font-family: "Montserrat", sans-serif;
    font-weight: 900;
    color: var(--black);
  }
  .fact-hex {
    position: relative;
    width: calc(28px * var(--s));
    height: calc(25px * var(--s));
  }
  .fact-hex svg { width: 100%; height: 100%; display: block; }
  .fact-hex polygon { fill: none; stroke: var(--black); stroke-width: 3; }
  .fact-value {
    position: absolute;
    inset: 0;
    display: flex;
    align-items: center;
    justify-content: center;
    font-size: calc(8px * var(--s));
  }
  .fact-name {
    font-size: calc(6.5px * var(--s));
    margin-top: calc(2px * var(--s));
    letter-spacing: 0.03em;
  }

  .flavour {
    position: absolute;
    left: 6%;
    bottom: 7%;
    font-family: "Bungee", sans-serif;
    font-size: calc(24px * var(--s));
    line-height: 1;
    color: var(--black);
  }
  .pack--pouch .flavour { left: 8%; bottom: 24%; }
  .flavour-sub {
    display: block;
    margin-left: 12%;
    font-size: calc(10px * var(--s));
    letter-spacing: 0.04em;
  }
</style>
</head>
<body>
<main class="range">

  <!-- Banana flavour set -->
  <section class="flavour-set flavour-set--banana">
    <article class="pack pack--tub">
      <svg class="pack-bg" viewBox="0 0 100 100" preserveAspectRatio="none" aria-hidden="true">
        <rect class="band-black" width="100" height="100"/>
        <polygon class="band-white" points="0,56 100,40 100,44 0,60"/>
        <polygon class="band-accent" points="0,60 100,44 100,100 0,100"/>
      </svg>
      <p class="brand">PULSEFORM</p>
      <p class="desc">DESCRIPTION OF PRODUCT</p>
      <div class="flavour-photo" role="img" aria-label="Photo of ripe bananas"></div>
      <ul class="facts">
        <li class="fact"><span class="fact-hex"><svg viewBox="0 0 40 36"><polygon points="10,2 30,2 38,18 30,34 10,34 2,18"/></svg><span class="fact-value">27G</span></span><span class="fact-name">PROTEIN</span></li>
        <li class="fact"><span class="fact-hex"><svg viewBox="0 0 40 36"><polygon points="10,2 30,2 38,18 30,34 10,34 2,18"/></svg><span class="fact-value">3G</span></span><span class="fact-name">PRODUCT 1</span></li>
        <li class="fact"><span class="fact-hex"><svg viewBox="0 0 40 36"><polygon points="10,2 30,2 38,18 30,34 10,34 2,18"/></svg><span class="fact-value">1G</span></span><span class="fact-name">PRODUCT 2</span></li>
      </ul>
      <p class="flavour">BANANA<span class="flavour-sub">FLAVOUR</span></p>
    </article>

    <article class="pack pack--jar">
      <svg class="pack-bg" viewBox="0 0 100 100" preserveAspectRatio="none" aria-hidden="true">
        <rect class="band-black" width="100" height="100"/>
        <polygon class="band-white" points="0,56 100,40 100,44 0,60"/>
        <polygon class="band-accent" points="0,60 100,44 100,100 0,100"/>
      </svg>
      <p class="brand">PULSEFORM</p>
      <p class="desc">DESCRIPTION OF PRODUCT</p>
      <div class="flavour-photo" role="img" aria-label="Photo of ripe bananas"></div>
      <ul class="facts">
        <li class="fact"><span class="fact-hex"><svg viewBox="0 0 40 36"><polygon points="10,2 30,2 38,18 30,34 10,34 2,18"/></svg><span class="fact-value">27G</span></span><span class="fact-name">PROTEIN</span></li>
        <li class="fact"><span class="fact-hex"><svg viewBox="0 0 40 36"><polygon points="10,2 30,2 38,18 30,34 10,34 2,18"/></svg><span class="fact-value">3G</span></span><span class="fact-name">PRODUCT 1</span></li>
        <li class="fact"><span class="fact-hex"><svg viewBox="0 0 40 36"><polygon points="10,2 30,2 38,18 30,34 10,34 2,18"/></svg><span class="fact-value">1G</span></span><span class="fact-name">PRODUCT 2</span></li>
      </ul>
      <p class="flavour">BANANA<span class="flavour-sub">FLAVOUR</span></p>
    </article>

    <article class="pack pack--pouch">
      <svg class="pack-bg" viewBox="0 0 100 100" preserveAspectRatio="none" aria-hidden="true">
        <rect class="band-black" width="100" height="100"/>
        <polygon class="band-accent" points="0,0 100,0 100,4 0,12"/>
        <polygon class="band-white" points="0,54 100,30 100,32 0,56"/>
        <polygon class="band-accent" points="0,56 100,32 100,100 0,100"/>
      </svg>
      <p class="brand">PULSEFORM</p>
      <p class="desc">DESCRIPTION OF PRODUCT</p>
      <div class="flavour-photo" role="img" aria-label="Photo of ripe bananas"></div>
      <ul class="facts">
        <li class="fact"><span class="fact-hex"><svg viewBox="0 0 40 36"><polygon points="10,2 30,2 38,18 30,34 10,34 2,18"/></svg><span class="fact-value">27G</span></span><span class="fact-name">PROTEIN</span></li>
        <li class="fact"><span class="fact-hex"><svg viewBox="0 0 40 36"><polygon points="10,2 30,2 38,18 30,34 10,34 2,18"/></svg><span class="fact-value">3G</span></span><span class="fact-name">PRODUCT 1</span></li>
        <li class="fact"><span class="fact-hex"><svg viewBox="0 0 40 36"><polygon points="10,2 30,2 38,18 30,34 10,34 2,18"/></svg><span class="fact-value">1G</span></span><span class="fact-name">PRODUCT 2</span></li>
      </ul>
      <p class="flavour">BANANA<span class="flavour-sub">FLAVOUR</span></p>
    </article>
  </section>

  <!-- Grape flavour set -->
  <section class="flavour-set flavour-set--grape">
    <article class="pack pack--tub">
      <svg class="pack-bg" viewBox="0 0 100 100" preserveAspectRatio="none" aria-hidden="true">
        <rect class="band-black" width="100" height="100"/>
        <polygon class="band-white" points="0,56 100,40 100,44 0,60"/>
        <polygon class="band-accent" points="0,60 100,44 100,100 0,100"/>
      </svg>
      <p class="brand">PULSEFORM</p>
      <p class="desc">DESCRIPTION OF PRODUCT</p>
      <div class="flavour-photo" role="img" aria-label="Photo of a bunch of green grapes"></div>
      <ul class="facts">
        <li class="fact"><span class="fact-hex"><svg viewBox="0 0 40 36"><polygon points="10,2 30,2 38,18 30,34 10,34 2,18"/></svg><span class="fact-value">27G</span></span><span class="fact-name">PROTEIN</span></li>
        <li class="fact"><span class="fact-hex"><svg viewBox="0 0 40 36"><polygon points="10,2 30,2 38,18 30,34 10,34 2,18"/></svg><span class="fact-value">3G</span></span><span class="fact-name">PRODUCT 1</span></li>
        <li class="fact"><span class="fact-hex"><svg viewBox="0 0 40 36"><polygon points="10,2 30,2 38,18 30,34 10,34 2,18"/></svg><span class="fact-value">1G</span></span><span class="fact-name">PRODUCT 2</span></li>
      </ul>
      <p class="flavour">GRAPE<span class="flavour-sub">FLAVOUR</span></p>
    </article>

    <article class="pack pack--jar">
      <svg class="pack-bg" viewBox="0 0 100 100" preserveAspectRatio="none" aria-hidden="true">
        <rect class="band-black" width="100" height="100"/>
        <polygon class="band-white" points="0,56 100,40 100,44 0,60"/>
        <polygon class="band-accent" points="0,60 100,44 100,100 0,100"/>
      </svg>
      <p class="brand">PULSEFORM</p>
      <p class="desc">DESCRIPTION OF PRODUCT</p>
      <div class="flavour-photo" role="img" aria-label="Photo of a bunch of green grapes"></div>
      <ul class="facts">
        <li class="fact"><span class="fact-hex"><svg viewBox="0 0 40 36"><polygon points="10,2 30,2 38,18 30,34 10,34 2,18"/></svg><span class="fact-value">27G</span></span><span class="fact-name">PROTEIN</span></li>
        <li class="fact"><span class="fact-hex"><svg viewBox="0 0 40 36"><polygon points="10,2 30,2 38,18 30,34 10,34 2,18"/></svg><span class="fact-value">3G</span></span><span class="fact-name">PRODUCT 1</span></li>
        <li class="fact"><span class="fact-hex"><svg viewBox="0 0 40 36"><polygon points="10,2 30,2 38,18 30,34 10,34 2,18"/></svg><span class="fact-value">1G</span></span><span class="fact-name">PRODUCT 2</span></li>
      </ul>
      <p class="flavour">GRAPE<span class="flavour-sub">FLAVOUR</span></p>
    </article>

    <article class="pack pack--pouch">
      <svg class="pack-bg" viewBox="0 0 100 100" preserveAspectRatio="none" aria-hidden="true">
        <rect class="band-black" width="100" height="100"/>
        <polygon class="band-accent" points="0,0 100,0 100,4 0,12"/>
        <polygon class="band-white" points="0,54 100,30 100,32 0,56"/>
        <polygon class="band-accent" points="0,56 100,32 100,100 0,100"/>
      </svg>
      <p class="brand">PULSEFORM</p>
      <p class="desc">DESCRIPTION OF PRODUCT</p>
      <div class="flavour-photo" role="img" aria-label="Photo of a bunch of green grapes"></div>
      <ul class="facts">
        <li class="fact"><span class="fact-hex"><svg viewBox="0 0 40 36"><polygon points="10,2 30,2 38,18 30,34 10,34 2,18"/></svg><span class="fact-value">27G</span></span><span class="fact-name">PROTEIN</span></li>
        <li class="fact"><span class="fact-hex"><svg viewBox="0 0 40 36"><polygon points="10,2 30,2 38,18 30,34 10,34 2,18"/></svg><span class="fact-value">3G</span></span><span class="fact-name">PRODUCT 1</span></li>
        <li class="fact"><span class="fact-hex"><svg viewBox="0 0 40 36"><polygon points="10,2 30,2 38,18 30,34 10,34 2,18"/></svg><span class="fact-value">1G</span></span><span class="fact-name">PRODUCT 2</span></li>
      </ul>
      <p class="flavour">GRAPE<span class="flavour-sub">FLAVOUR</span></p>
    </article>
  </section>

</main>
</body>
</html>
```